Billboard design

Loom Rinse Master, needs a new design for 10' x 40' billboard. The design picked will also be used on a 2014 white Halvik Courier Van.

Design needs to be clean and easy to read and include existing logo and phone number...318-742-6093. We specialize in washing rugs...not carpet cleaning, so don't submit designs of a carpet cleaning machine on rugs. Rugs are submerged in water in a pit, scrubbed, rinsed and extracted. Most rugs are dirty due to pet problems. This is our 25th year in business so that may also be included. Our customers are generally higher end income women over 30.

Simply put our logo as the largest print, with the phone number second largest. No other text is needed. Just layout and graphics. Ideally a rug with an animal on it, or a dirty rug with dog, dirty dog, dog scooting on rug, food spill, etc...

I also would be interested in seeing a billboard that looks like an oriental rug with the center faded out with our logo. Rug needs to look very high end. I don't want clip art or a cartoony look.

Keep in mind that this same look will be used on all company vans.
Updates

                                       Our logo should be the only text, besides the phone number.  I just need graphics and a nice clean layout, that is very easy to read from the road.  25 yrs can also be included.

Please make sure my logo is very large.  If you put in a photo of a rug, make sure it looks like a rug and not wall to wall carpet.                                   

Reason: On vacation till Tue. 18.

Reason: Not happy with designs so far. Lots of the designs sent look as though a child sent them. There are a couple that are good. In addition to the brief that I left earlier, I would like to see maybe a sketch of a mischievous dog on a simple sketched rug. Could possibly use this as a mascot. I am considering getting rid of the blue drop in the logo. VERY SIMPLE clean design with very few lines in the sketch.

Target Market(s)

Women over 30, higher income

Industry/Entity Type

Pet

Requirements
Nice to have
• Dog on oriental rug, scooting, or dirty, or funny face etc...
Should not have
• Cartoon

```html
<!DOCTYPE html>
<html lang="en">
<head>
<meta charset="utf-8">
<title>Loom Rinse Master – Billboard</title>
<link rel="stylesheet" href="https://fonts.googleapis.com/css2?family=Arimo:wght@700&family=Open+Sans:wght@400;700&display=swap">
<style>
  :root {
    --paper: #ffffff;
    --wave-light: #e3eef8;
    --wave-mid: #c9ddef;
    --wave-grey: #d9d9d9;
    --banner: #fdb913;
    --banner-shade: #d99a00;
    --ink: #111111;
    --brand-grey: #4a4a4a;
    --sub-grey: #666666;
    --accent-red: #ee1c1c;
    --mark-blue: #4f96d0;
  }
  html, body {
    margin: 0;
    padding: 0;
    overflow: hidden;
    background: var(--paper);
  }
  .billboard {
    position: relative;
    width: 1200px;
    height: 300px;
    overflow: hidden;
    background: var(--paper);
  }
  .billboard__waves {
    position: absolute;
    inset: 0;
  }
  .call-banner__text {
    position: absolute;
    left: 22px;
    top: 160px;
    font-family: "Arimo", Arial, sans-serif;
    font-weight: 700;
    color: var(--ink);
    line-height: 1;
  }
  .call-banner__label {
    font-size: 34px;
    margin-bottom: 10px;
  }
  .call-banner__phone {
    font-size: 58px;
    letter-spacing: -0.5px;
  }
  .brand {
    position: absolute;
    left: 504px;
    top: 66px;
    display: flex;
    align-items: center;
    gap: 18px;
  }
  .brand__dot {
    width: 80px;
    height: 80px;
    border-radius: 50%;
    background: var(--mark-blue);
    flex: none;
  }
  .brand__words {
    display: flex;
    flex-direction: column;
    align-items: flex-end;
  }
  .brand__name {
    font-family: "Open Sans", Arial, sans-serif;
    font-weight: 700;
    font-size: 64px;
    color: var(--brand-grey);
    line-height: 1;
    letter-spacing: -1.5px;
    white-space: nowrap;
  }
  .brand__company {
    font-family: "Open Sans", Arial, sans-serif;
    font-weight: 400;
    font-size: 22px;
    color: var(--sub-grey);
    margin-top: 6px;
    white-space: nowrap;
  }
  .since {
    position: absolute;
    right: 22px;
    bottom: 14px;
    font-family: "Arimo", Arial, sans-serif;
    font-weight: 700;
    color: var(--ink);
    font-size: 27px;
    line-height: 1;
    display: flex;
    align-items: baseline;
    gap: 10px;
  }
  .since__years {
    color: var(--accent-red);
    font-size: 54px;
  }
</style>
</head>
<body>
  <div class="billboard">
    <svg class="billboard__waves" width="1200" height="300" viewBox="0 0 1200 300" aria-hidden="true">
      <path d="M0 60 C 120 70, 260 120, 380 170 L 380 185 C 250 135, 120 90, 0 85 Z" fill="var(--wave-grey)"/>
      <path d="M300 190 C 520 110, 800 70, 1200 110 L 1200 250 C 900 200, 600 200, 300 250 Z" fill="var(--wave-light)"/>
      <path d="M420 200 C 640 140, 900 120, 1200 150 L 1200 175 C 920 150, 660 170, 420 220 Z" fill="var(--wave-mid)"/>
      <path d="M350 250 C 620 205, 900 215, 1200 245 L 1200 300 L 350 300 Z" fill="var(--paper)"/>
      <path d="M500 260 C 720 230, 950 232, 1200 262 L 1200 270 C 950 242, 720 240, 500 268 Z" fill="var(--wave-grey)"/>
      <polygon points="0,146 452,146 500,216 452,288 0,288" fill="var(--banner-shade)"/>
      <polygon points="0,142 448,142 494,210 448,280 0,280" fill="var(--banner)"/>
    </svg>

    <div class="call-banner__text">
      <div class="call-banner__label">Call :</div>
      <div class="call-banner__phone">318-742-6093</div>
    </div>

    <div class="brand">
      <div class="brand__dot"></div>
      <div class="brand__words">
        <div class="brand__name">Loom Rinse Master</div>
        <div class="brand__company">BRIGHTWELL CLEANING, LLC</div>
      </div>
    </div>

    <div class="since">
      <span>SINCE</span>
      <span class="since__years">25</span>
      <span>YEARS</span>
    </div>
  </div>
</body>
</html>
```